Facebook Header Design Project.

I'm supplying white and colored logos. The Facebook page already exists. URL = https://www.pagebook.example/lumocrest.design The design should not be based on what's already there. Consider mobile implications of the design. This Design will form the designs of other social media headers. LumoCrest is a web design | digital marketing company.

Target Market(s)

People interested in web design | digital marketing services.

Industry/Entity Type

LumoCrest is a web design | digital marketing company. That should be clear in the design.

Colors
0054AA
0677BA
7BADD7
CADEEF
E8F1F8

Requirements
Must have
• Logo. Use Facebook header image dimension.
Nice to have
• Use a color scheme like the logo and feel free to add a color or two from the other side of the color whee.

```html
<!DOCTYPE html>
<html lang="en">
<head>
<meta charset="utf-8">
<title>LumoCrest – Web Design &amp; Digital Marketing Header</title>
<link rel="stylesheet" href="https://fonts.googleapis.com/css2?family=Josefin+Sans:wght@600;700&family=Great+Vibes&family=Lato:wght@700&display=swap">
<style>
  :root {
    --stage: #0c1630;
    --banner-blue: #1a36a2;
    --blob-blue: #0a62b8;
    --cyan: #0dd3f6;
    --band-blue: #2f6bf0;
    --photo-light: #e9ecef;
    --photo-mid: #c9d6e4;
    --white: #ffffff;
    --frame: #ffffff;
  }
  * { box-sizing: border-box; margin: 0; padding: 0; }
  html, body { width: 1200px; height: 744px; overflow: hidden; background: var(--stage); }
  .stage { position: relative; width: 1200px; height: 744px; background: var(--stage); }
  .cover {
    position: absolute; left: 67px; top: 174px; width: 1066px; height: 396px;
    border: 2px solid var(--frame); background: var(--banner-blue); overflow: hidden;
  }
  .cover-shapes { position: absolute; inset: 0; width: 100%; height: 100%; }
  .brand {
    position: absolute; left: 56px; top: 34px;
    font-family: "Josefin Sans", sans-serif; font-weight: 700; font-size: 34px;
    line-height: 40px; color: var(--white); letter-spacing: 0.5px;
  }
  .headline {
    position: absolute; left: 52px; top: 104px;
    font-family: "Josefin Sans", sans-serif; font-weight: 700; font-size: 40px;
    line-height: 51px; color: var(--white); text-transform: uppercase; white-space: nowrap;
  }
  .headline-script {
    position: absolute; left: 50px; top: 204px;
    font-family: "Great Vibes", cursive; font-size: 80px; line-height: 70px;
    color: var(--white); white-space: nowrap;
  }
  .intro {
    position: absolute; left: 52px; top: 278px; width: 392px;
    font-family: "Lato", sans-serif; font-weight: 700; font-size: 12.5px;
    line-height: 16.5px; color: var(--white); letter-spacing: -0.3px;
  }
  .social-list { position: absolute; left: 52px; top: 347px; display: flex; gap: 17px; list-style: none; }
  .social-list li { width: 24px; height: 24px; border-radius: 50%; background: var(--white); }
</style>
</head>
<body>
<main class="stage">
  <section class="cover" aria-label="LumoCrest page header">
    <svg class="cover-shapes" viewBox="0 0 1066 396" preserveAspectRatio="none">
      <defs>
        <linearGradient id="photoTone" x1="0" y1="0" x2="1" y2="1">
          <stop offset="0" stop-color="var(--photo-light)"/>
          <stop offset="0.55" stop-color="var(--photo-mid)"/>
          <stop offset="1" stop-color="#f4f5f6"/>
        </linearGradient>
      </defs>
      <rect class="dot-grid" x="12" y="12" width="96" height="140" fill="#ffffff" opacity="0.04" role="img" aria-label="Dot grid pattern"/>
      <path class="top-blob" d="M296,0 H600 L520,96 Q460,88 420,94 Q350,104 322,72 Q304,40 296,0 Z" fill="var(--blob-blue)"/>
      <path class="cyan-band" d="M557,0 H720 L600,70 L520,110 L470,110 Q476,40 557,0 Z" fill="var(--cyan)"/>
      <path class="accent-band" d="M470,104 Q474,92 496,92 L580,92 L720,396 H617 L480,144 Q466,122 470,104 Z" fill="var(--band-blue)"/>
      <path class="photo-area" d="M632,0 H1066 V396 H659 L512,128 Q498,100 524,84 Z" fill="url(#photoTone)" role="img" aria-label="Photo: smiling man in a light blue shirt working on a laptop at a white desk with a mug, notebook and a potted plant"/>
      <rect class="dot-grid" x="311" y="341" width="73" height="38" fill="#ffffff" opacity="0.05" role="img" aria-label="Dot grid pattern"/>
      <rect class="plus-grid" x="508" y="336" width="50" height="48" fill="#ffffff" opacity="0.05" role="img" aria-label="Plus sign grid pattern"/>
    </svg>

    <div class="brand">LumoCrest</div>
    <h1 class="headline">Web Design &amp;<br>Digital Marketing</h1>
    <p class="headline-script">Services</p>
    <p class="intro">Lorem Ipsum is simply dummy text of the printing and typesetting industry. Lorem has been the industry's standard dummy text ever since the 1500s</p>
    <ul class="social-list" aria-label="Social channels, including https://www.pagebook.example/lumocrest.design">
      <li></li><li></li><li></li><li></li>
    </ul>
  </section>
</main>
</body>
</html>
```